Visitenkarten-Design für German Consulting Company
Zielgruppe
We are a German Consulting Company, who specialized in public sector Software development (www.qrt-beratung.de).
Our customers are audit offices all over Germany. We offer 3 custom software solution’s to our customers. Those three software solutions form a Software-Suite.
Our three products are called: qrt clearScope, qrt ledgerPilot and qrt ledgerWriter..
You can find the 3 Logos for our products enclosed
Wir sind eine Unternehmensberatung, die sich auf Softwareentwicklung für den Public Sektor spezialisiert hat (www.qrt-beratung.de). Unsere Zielgruppe sind Rechnungsprüfungsämter in ganz Deutschland. Wir bieten für diesen Markt drei abgestimmte Softwareprodukte an, die zusammen eine Software-Suite bilden. Die drei Produkte sind der qrt clearScope, der qrt ledgerWriter und der qrt ledgerPilot.
Aufgabenstellung
For activation, our software needs a licence key. This Key is sent to our customers with a nice box an the requird documentation.
The licence Key is supposed to be printed onto a metal card.
We are looking for a design regarding those „licencecards“
You can find the avaliable options for materials and customizations here: https://www.karten-stahl-vp.example/optionen/
The card has at least to show the following Information’s:
Company Logo and
licencekey: 8416 9072 5831 6049
We are going for a clean, professional and high value look.
Unsere Produkte benötigen einen Lizenzschlüssel um aktiviert zu werden. Dieser Lizenzschlüssel wird mit den dazugehörigen Handbüchern in einer edlen Verpackung übergeben. Der Lizenzschlüssel soll auf einer Metallkarte aufgebracht werden, wie Sie diese Firma anbietet: https://www.karten-stahl-vp.example/.
Materialien und Verabreitungsmöglichkeiten werden hier aufgeführt: https://www.karten-stahl-vp.example/optionen/
Die Karte muss mindestens unser Firmenlogo und eine 16 Stellige Lizenznummer(8416 9072 5831 604) enthalten.
Die Karte soll clean, professionell und hochwertig aussehen und wenige Farben verwenden .

```html
<!DOCTYPE html>
<html lang="de">
<head>
<meta charset="utf-8">
<title>qrt Lizenzkarte</title>
<link href="https://fonts.googleapis.com/css2?family=Open+Sans:wght@400;600;700&display=swap" rel="stylesheet">
<style>
  :root {
    --bg: #c4bebe;
    --card: #efeeec;
    --ink: #1e1e1e;
    --ink-soft: #3a3a3a;
    --accent: #d8141e;
  }
  html, body {
    margin: 0;
    width: 1200px;
    height: 818px;
    overflow: hidden;
    background: var(--bg);
    font-family: "Open Sans", Arial, sans-serif;
    color: var(--ink);
  }
  .stage { position: relative; width: 1200px; height: 818px; }
  .card {
    position: absolute;
    top: 248px;
    width: 500px;
    height: 323px;
    background: var(--card);
    box-shadow: 0 6px 18px rgba(0,0,0,.12);
    box-sizing: border-box;
  }
  .card--front { left: 70px; }
  .card--back { left: 630px; }

  /* Front: licence key */
  .licence { position: absolute; left: 36px; top: 40px; }
  .licence__title {
    font-weight: 700;
    font-size: 17px;
    letter-spacing: .5px;
    margin: 0;
  }
  .licence__key {
    font-size: 13px;
    margin: 2px 0 0;
    color: var(--ink-soft);
    letter-spacing: .3px;
  }
  .rule {
    position: absolute;
    right: 0;
    height: 1px;
    background: var(--accent);
  }
  .rule--top { left: 214px; top: 61px; }
  .rule--bottom { left: 300px; top: 270px; }
  .brand {
    position: absolute;
    left: 36px;
    top: 252px;
    font-weight: 700;
    font-size: 17px;
    color: var(--ink);
    display: flex;
    align-items: center;
    gap: 8px;
  }
  .brand__mark {
    width: 12px; height: 12px;
    background: var(--accent);
  }

  /* Back: contact details */
  .contact {
    position: absolute;
    left: 36px;
    top: 34px;
    font-size: 11px;
    line-height: 1.5;
    color: var(--ink-soft);
  }
  .contact p { margin: 0; }
  .contact__name { font-weight: 600; color: var(--ink); }
  .contact__row { display: flex; align-items: center; gap: 5px; }
  .contact__company { margin-top: 44px !important; font-weight: 600; color: var(--ink); }
  .contact__label { margin-top: 16px !important; font-weight: 600; color: var(--ink); }
  .contact__web { margin-top: 16px !important; }
  .icon { width: 10px; height: 10px; flex: none; }
</style>
</head>
<body>
<main class="stage">
  <section class="card card--front" aria-label="Lizenzkarte Vorderseite">
    <div class="licence">
      <h1 class="licence__title">LIZENSSCHLÜSSEL</h1>
      <p class="licence__key">8416 9072 5831 6049</p>
    </div>
    <div class="rule rule--top"></div>
    <div class="brand"><span class="brand__mark"></span>qrt quandt, roth &amp; teubner</div>
    <div class="rule rule--bottom"></div>
  </section>

  <section class="card card--back" aria-label="Lizenzkarte Rückseite">
    <div class="contact">
      <p class="contact__name">Dr. Markus Korbel / Geschäftsführer</p>
      <p class="contact__row">
        <svg class="icon" viewBox="0 0 10 10"><path d="M2 1 L4 1 L4.6 3 L3.4 3.8 Q4.4 5.8 6.2 6.6 L7 5.4 L9 6 L9 8 Q5 9 2 5.5 Q1 3.5 2 1Z" fill="var(--accent)"/></svg>
        0049 6171 40522 202
        <svg class="icon" viewBox="0 0 10 10"><rect x="0.5" y="2" width="9" height="6" fill="var(--accent)"/><path d="M0.5 2 L5 5.5 L9.5 2" stroke="#fff" stroke-width="1" fill="none"/></svg>
        m.korbel@qrt-beratung.de
      </p>
      <p class="contact__company">qrt Informationssysteme GmbH · Innovationspark</p>
      <p>Lindenallee 14 · 61440 Oberursel</p>
      <p class="contact__label">Zentrale:</p>
      <p>0049 6171 40522 0</p>
      <p>info@qrt-beratung.de</p>
      <p class="contact__row contact__web">
        <svg class="icon" viewBox="0 0 10 10"><circle cx="5" cy="5" r="4.5" fill="var(--accent)"/><path d="M0.5 5 H9.5 M5 0.5 V9.5 M5 0.5 Q2 5 5 9.5 M5 0.5 Q8 5 5 9.5" stroke="#fff" stroke-width=".6" fill="none"/></svg>
        www.qrt-beratung.de
      </p>
    </div>
  </section>
</main>
</body>
</html>
```